Consulting Firm stationery design

Now that the MakerHive has given us a new logo we'll now need to have all our stationery designed. So we're asking for this community to help us once again.We're looking to get from you Letterheads (Header and Footer, suitable to be applied on a .docx format. Vectors are required but keep this in mind), Envelopes (Front and Back designs, back is not a must but desirable depending on your design), 9"x 12" Pocket Folders (consider design for front and back, also for pockets as well), Business Cards.An elegant design is a must have, mostly for Folders and Envelopes. The idea with this two is to stand out from others when they're handed over. Ideas are welcomed, we were thinking maybe on some texturing simulation for these.Folders will have 3 addresses and contact information. Envelopes will have 1 address and contact information.Brand Manual attached. vendaluxo logo has been copyrighted already. I'm also attaching the current stationary designs (these never got to be out for production but was going to be before we made the brand changes); Pocker folders page 1 to 4 (pages 2 and 4 are the pocket designs), Pages 5 and 6 (6 is the back of the envelope), Pages 7 and 8 (8 is the back of the business card). No letterhead within these designs as it just had the logo and address.

Industry/Entity Type

Business Consultant

Font styles to use
Serif
Sans Serif

Requirements
Must have
• Elegance
Nice to have
• Modern looking out of common

```html
<!DOCTYPE html>
<html lang="es">
<head>
<meta charset="utf-8">
<title>vendaluxo — Letterhead</title>
<link href="https://fonts.googleapis.com/css2?family=Open+Sans:wght@400;600;700&display=swap" rel="stylesheet">
<style>
  :root {
    --brand-blue: #0a78b5;
    --brand-navy: #2b2e3b;
    --header-grey: #d9d9d9;
    --body-text: #474a52;
    --footer-text: #6b6e75;
    --backdrop: #e6e7ea;
    --paper: #ffffff;
  }
  * { margin: 0; padding: 0; box-sizing: border-box; }
  html, body {
    width: 1200px; height: 1200px; overflow: hidden;
    background: var(--backdrop);
    font-family: "Open Sans", Arial, sans-serif;
  }
  .letterhead {
    position: absolute; left: 167px; top: 40px;
    width: 866px; height: 1120px;
    background: var(--paper);
    box-shadow: 0 6px 24px rgba(0,0,0,.18);
    overflow: hidden;
  }
  .header-band {
    position: absolute; left: 390px; top: 0; right: 0; height: 205px;
    background: var(--header-grey);
  }
  .brand-name {
    position: absolute; left: 42px; top: 110px;
    font-size: 52px; font-weight: 700; letter-spacing: -1px;
    color: var(--brand-navy);
    display: flex; align-items: center; gap: 12px;
  }
  .brand-dot {
    width: 16px; height: 16px; border-radius: 50%;
    background: var(--brand-blue);
  }
  .brand-rule {
    position: absolute; left: 36px; top: 236px; width: 246px; height: 4px;
    background: var(--brand-blue);
  }
  .side-column {
    position: absolute; left: 36px; top: 262px; width: 250px; bottom: 0;
    background: var(--brand-blue);
  }
  .side-text {
    position: absolute; left: 68px; top: 352px; width: 196px;
    color: #fff; font-size: 15.5px; line-height: 21px;
    text-align: justify; text-indent: 40px;
  }
  .letter-body {
    position: absolute; left: 320px; top: 296px; width: 510px;
    color: var(--body-text); font-size: 19px; line-height: 33px;
  }
  .letter-body p { text-align: justify; text-indent: 36px; }
  .letter-body .salutation { text-indent: 0; }
  .signature {
    position: absolute; left: 650px; top: 772px;
    color: var(--body-text); font-size: 21px; line-height: 34px;
  }
  .signature-rule {
    position: absolute; left: 650px; top: 846px; width: 150px; height: 2px;
    background: var(--brand-blue);
  }
  .footer-rule {
    position: absolute; left: 300px; top: 940px; width: 534px; height: 6px;
    background: var(--brand-blue);
  }
  .footer-address {
    position: absolute; left: 620px; top: 968px;
    color: var(--footer-text); font-size: 13.5px; font-weight: 700; line-height: 23px;
    font-style: normal;
  }
  .social-links {
    position: absolute; left: 620px; top: 1050px; display: flex; gap: 12px;
  }
  .social-links span {
    width: 20px; height: 20px; border-radius: 4px; background: var(--footer-text);
  }
</style>
</head>
<body>
  <main class="letterhead">
    <div class="header-band"></div>

    <div class="brand-name">vendaluxo<span class="brand-dot"></span></div>
    <div class="brand-rule"></div>

    <aside class="side-column"></aside>
    <p class="side-text">Qui exercitation nulla occaecat laboris pariatur est consequat dolor do, adipisicing amet minim nisi. In excepteur in do. Anim adipisicing pariatur ut ut non nisi fugiat esse. Labore in, est lorem, in minim irure qui labore elit, proident dolore id.</p>

    <section class="letter-body">
      <p class="salutation">Dear Mr. Halloway,</p>
      <p>Qui exercitation nulla occaecat laboris pariatur est consequat dolor do, adipisicing amet minim nisi. In excepteur in do. Anim adipisicing pariatur ut ut non nisi fugiat esse. Labore in, est lorem, in minim irure qui labore elit, proident dolore id.</p>
      <p>Adipisicing in ad aliquip ullamco mollit. Sint tempor eu magna ea sunt commodo voluptate sint, magna non exercitation aliqua amet irure, laboris consectetur. Sunt velit ut dolore sunt, eu sit adipisicing commodo ut sint officia proident lorem officia. Culpa id labore nisi ad. Consectetur sint, in ad aute velit, enim lorem dolor veniam occaecat nulla excepteur aliqua nostrud?</p>
    </section>

    <div class="signature">Best regards,<br>R. Whitmore</div>
    <div class="signature-rule"></div>

    <div class="footer-rule"></div>
    <address class="footer-address">
      DO | Ave. Las Palmas 42<br>
      Torre Norvik Work, 3er Nivel<br>
      Santo Domingo, D.N.
    </address>
    <div class="social-links" aria-label="Social media links">
      <span></span><span></span><span></span><span></span>
    </div>
  </main>
</body>
</html>
```